Email Signature

We are looking for creative email signature for our company. Please find attached the logo of our company for your reference. now we understand there isn't much can be done with email signature but we are looking for out of the box designs. Nothing specific in mind

Please insert fake numbers, website and/or address, etc just to showcase the designs. once the design is chosen we will provide the actual details.
Updates

Dear All,

We wouldlike to extend our apology for not being able to provide feedbacks to everysingle design. We were extremely busy and we have multiple contests opensimultaneously which makes the process harder. However, thank you all for theefforts you have put into this contest. We have received anoverwhelming quality responses & it has been a very difficult task tochoose just one, we easily Loved at least several designs...

Thanksagain for participating, we wish you all success in your design ventures.

Kindregards,

KLC Team

Industry/Entity Type

It Company

```html
<!DOCTYPE html>
<html lang="en">
<head>
<meta charset="utf-8">
<title>TradeLoop Email Signature</title>
<link href="https://fonts.googleapis.com/css2?family=Arimo:wght@400;700&display=swap" rel="stylesheet">
<style>
  :root {
    --ink: #111111;
    --link: #3a6ea8;
    --brand-blue: #3a6ea8;
    --brand-green: #5db234;
    --paper: #ffffff;
    --backdrop-light: #f7f7f7;
    --backdrop-dark: #e2e2e2;
    --panel-edge: #dcdcdc;
  }
  * { margin: 0; padding: 0; box-sizing: border-box; }
  html, body { width: 1200px; height: 939px; overflow: hidden; }
  body {
    position: relative;
    font-family: "Arimo", Arial, Helvetica, sans-serif;
    color: var(--ink);
    background: radial-gradient(ellipse at 50% 95%, var(--backdrop-light) 0%, var(--backdrop-dark) 100%);
  }
  .signature {
    position: absolute;
    left: 20px; top: 14px;
    width: 1161px; height: 777px;
    background: var(--paper);
    border: 1px solid var(--panel-edge);
  }
  .block { position: absolute; font-size: 23.5px; line-height: 29px; }
  .greeting { left: 42px; top: 50px; }
  .person { left: 42px; top: 136px; }
  .person-name {
    display: block;
    font-size: 30px; line-height: 36px; font-weight: 700;
    color: var(--link); text-decoration: underline;
    text-underline-offset: 3px; text-decoration-thickness: 2px;
  }
  .direct { left: 42px; top: 241px; }
  .company-mark {
    position: absolute; left: 48px; top: 400px;
    display: flex; align-items: center; gap: 12px;
  }
  .mark-dot { width: 26px; height: 26px; border-radius: 50%; background: var(--brand-green); }
  .mark-name { font-size: 34px; font-weight: 700; color: var(--brand-blue); }
  .company { left: 311px; top: 350px; }
  .company-name { font-weight: 700; }
  .gap { display: block; height: 29px; }
  .bank { left: 42px; top: 596px; }
  a { color: var(--link); text-decoration: none; }
  .footer-mark {
    position: absolute; right: 36px; top: 852px;
    display: flex; align-items: center; gap: 14px;
  }
  .footer-mark .mark-dot { width: 40px; height: 40px; background: var(--brand-blue); }
  .footer-mark .mark-name { font-size: 46px; color: var(--brand-green); }
</style>
</head>
<body>
  <section class="signature">
    <p class="block greeting">Met vriendelijke groet,<br>Your sincerely,</p>
    <p class="block person">
      <a class="person-name" href="#">Ben Aalders</a>
      Operational Manager
    </p>
    <p class="block direct">
      E mail : <a href="#">baalders@tradeloop.example</a><br>
      Mobile +62 300 11122
    </p>
    <div class="company-mark">
      <span class="mark-dot"></span>
      <span class="mark-name">TradeLoop</span>
    </div>
    <p class="block company">
      <span class="company-name">TradeLoop</span><br>
      Stillwater 412 B, 55231KR Merin (MR)<br>
      Post 3321, 55231KR Merin (MR)
      <span class="gap"></span>
      Phone +62 300 11122<br>
      Fax +62 300 11122<br>
      E mail <a href="#">www.tradeloop.example</a>
    </p>
    <p class="block bank">
      Keltbank<br>
      KpK 00045600<br>
      CPNS HTR4040.987.654.00<br>
      <a href="#">www.tradeloop.example</a>
    </p>
  </section>
  <div class="footer-mark">
    <span class="mark-dot"></span>
    <span class="mark-name">TradeLoop</span>
  </div>
</body>
</html>
```